Poster for Wobble Evening - a weekly comedy/variety show

We would like a poster/postcard design for a weekly alternative comedy/variety show called Wobble Evening.
Style: The poster should be fun and eye catching and very bold. It should have an alternative feel, not mainstream. Weird, strange, bizarre and funny is good. The show's title "Wobble Evening" should be very prominent. I like the idea of it being busy and cartoony, a collage of weirdness. Fenwick Dabble's Spinning Carnival or Cpt. Quimby's Restless Ankle's Parade Troupe or psychedelic rock posters of the 70's.
Design Specifics: We are looking for one design that can both be on an 11" x 17" poster and reduced to a 4" x 6" postcard.
The copy:
-
vtm productions presents:
Wobble Evening
standup, music, storytelling, sketch and improv
Wednesdays @ Gullfeather Theatre
5164 W. Larkmont - 2nd Floor
Chicago, IL 60588
7:30 - The Loose Hour
8:30 - The Medley Hour
9:45 - Torbeck Ladder
Pay what you want
website: wobbleevening.example
-
The back of the postcard can be very simple. We may add stickers to it regularly with the specific dates and the names of guest performers.
UPDATE: I've updated the copy a little bit and made this a guaranteed contest.
Reason: I asked a couple designers to submit changes and have extended the deadline so that they have time to do that.
I have picked a design and I'm just now going to try to choose between the variations of that poster that the designer posted. No need to add any more designs unless I request them directly.
Young adults (20s-40s), college students, living on the north side of Chicago who are looking for a fun, inexpensive, cool night out during the week.
Club

```html
<!DOCTYPE html>
<html lang="en">
<head>
<meta charset="utf-8">
<title>Wobble Evening — Weekly Comedy &amp; Variety</title>
<link rel="stylesheet" href="https://fonts.googleapis.com/css2?family=Bebas+Neue&family=Oswald:wght@500;600;700&display=swap">
<style>
  :root {
    --backdrop: #e4e4e4;
    --paper: #f4e4ca;
    --paper-edge: #ecd7b6;
    --orange: #f2a35e;
    --orange-deep: #c96d31;
    --orange-ribbon: #eb9c55;
    --brown: #5b2b1b;
    --brown-text: #8a4524;
    --sky: #9ad7e2;
    --sky-deep: #63b3c3;
    --dash: #a98a74;
  }
  * { margin: 0; padding: 0; box-sizing: border-box; }
  html, body { width: 1200px; height: 816px; overflow: hidden; }
  body {
    background: var(--backdrop);
    font-family: "Oswald", "Arial Narrow", sans-serif;
    position: relative;
  }

  .poster {
    position: absolute;
    left: 350px; top: 30px;
    width: 500px; height: 756px;
    background: radial-gradient(ellipse at 50% 40%, var(--paper) 55%, var(--paper-edge) 100%);
    text-align: center;
    color: var(--brown);
  }
  .poster__frame {
    position: absolute; inset: 10px;
    border: 2px dashed var(--dash);
    pointer-events: none;
  }

  .banner { position: absolute; left: 50%; transform: translateX(-50%); }
  .banner svg { position: absolute; inset: 0; width: 100%; height: 100%; }
  .banner__text {
    position: relative;
    display: block;
    font-weight: 600;
    text-transform: uppercase;
    white-space: nowrap;
  }

  .presenter { top: 30px; width: 270px; height: 32px; }
  .presenter .banner__text { font-size: 17px; line-height: 30px; color: var(--brown); letter-spacing: .2px; }

  .show-title {
    position: absolute; left: 0; right: 0; top: 82px;
    font-family: "Bebas Neue", "Oswald", sans-serif;
    font-size: 88px; line-height: 1;
    color: var(--orange);
    letter-spacing: 1px;
    text-shadow: 1px 1px 0 var(--orange-deep), 2px 2px 0 var(--orange-deep), 3px 3px 0 var(--orange-deep);
  }

  .genres { top: 203px; width: 424px; height: 26px; }
  .genres .banner__text { font-size: 13.5px; line-height: 26px; color: #f6e6cc; font-weight: 500; }
  .genres .dot { color: var(--orange); margin: 0 3px; }

  .night {
    position: absolute; left: 0; right: 0; top: 240px;
    font-family: "Bebas Neue", "Oswald", sans-serif;
    font-size: 70px; line-height: 1;
    color: var(--orange);
    text-shadow: 1px 1px 0 var(--orange-deep), 2px 2px 0 var(--orange-deep), 3px 3px 0 var(--orange-deep);
  }
  .venue {
    position: absolute; left: 0; right: 0; top: 316px;
    font-size: 23px; font-weight: 600; text-transform: uppercase; color: var(--brown);
  }
  .address { top: 356px; width: 370px; height: 24px; }
  .address .banner__text { font-size: 14px; line-height: 24px; color: var(--brown); }

  .lineup {
    position: absolute; left: 102px; top: 418px;
    list-style: none;
  }
  .lineup::before {
    content: ""; position: absolute; left: 31px; top: 30px; bottom: 30px;
    width: 3px; background: var(--orange);
  }
  .lineup__slot {
    position: relative;
    display: flex; align-items: center;
    height: 64px; margin-bottom: 9px;
  }
  .lineup__time {
    width: 64px; height: 64px; border-radius: 50%;
    background: var(--brown); color: var(--sky);
    font-size: 25px; font-weight: 500; line-height: 64px;
    flex: none;
  }
  .lineup__act {
    margin-left: 16px;
    font-size: 35px; font-weight: 600; text-transform: uppercase;
    color: var(--brown-text);
    text-shadow: 1px 1px 0 #5b2b1b55;
  }

  .price { position: absolute; left: 82px; top: 660px; width: 340px; height: 80px; }
  .price svg { position: absolute; inset: 0; width: 100%; height: 100%; overflow: visible; }
  .price__line {
    position: absolute;
    font-size: 17px; font-weight: 600; text-transform: uppercase; color: var(--brown);
    transform: rotate(-13deg); white-space: nowrap;
  }
  .price__line--pay { left: 34px; top: 18px; }
  .price__line--min { left: 176px; top: 27px; }
</style>
</head>
<body>
  <main class="poster">
    <div class="poster__frame"></div>

    <div class="banner presenter">
      <svg viewBox="0 0 270 32" aria-hidden="true">
        <polygon points="0,8 30,8 30,30 0,30 9,19" fill="var(--sky-deep)"/>
        <polygon points="270,8 240,8 240,30 270,30 261,19" fill="var(--sky-deep)"/>
        <polygon points="22,24 30,30 30,24" fill="var(--brown)"/>
        <polygon points="248,24 240,30 240,24" fill="var(--brown)"/>
        <rect x="22" y="2" width="226" height="23" fill="var(--sky)"/>
      </svg>
      <span class="banner__text">vtm productions presents</span>
    </div>

    <h1 class="show-title">Wobble Evening</h1>

    <div class="banner genres">
      <svg viewBox="0 0 424 26" aria-hidden="true">
        <polygon points="0,13 12,0 412,0 424,13 412,26 12,26" fill="var(--brown)"/>
        <polygon points="6,13 13,7 13,19" fill="var(--orange)"/>
        <polygon points="418,13 411,7 411,19" fill="var(--orange)"/>
      </svg>
      <span class="banner__text">Improv<span class="dot">•</span>Standup<span class="dot">•</span>Music<span class="dot">•</span>Storytelling<span class="dot">•</span>Sketch and more</span>
    </div>

    <h2 class="night">Wednesdays</h2>
    <p class="venue">@ Gullfeather Theatre</p>

    <div class="banner address">
      <svg viewBox="0 0 370 24" aria-hidden="true" style="overflow:visible">
        <polyline points="-4,4 -12,12 -4,20" fill="none" stroke="var(--orange)" stroke-width="2"/>
        <polyline points="374,4 382,12 374,20" fill="none" stroke="var(--orange)" stroke-width="2"/>
        <polygon points="0,12 12,0 358,0 370,12 358,24 12,24" fill="var(--sky)"/>
      </svg>
      <span class="banner__text">5164 W. Larkmont - 2nd Floor Chicago, IL 60588</span>
    </div>

    <ul class="lineup">
      <li class="lineup__slot"><span class="lineup__time">7:30</span><span class="lineup__act">The Loose Hour</span></li>
      <li class="lineup__slot"><span class="lineup__time">8:30</span><span class="lineup__act">The Medley Hour</span></li>
      <li class="lineup__slot"><span class="lineup__time">9:45</span><span class="lineup__act">Torbeck Ladder</span></li>
    </ul>

    <div class="price">
      <svg viewBox="0 0 340 80" aria-hidden="true">
        <polygon points="0,58 14,44 4,34 170,-4 176,24 16,64" fill="var(--orange-ribbon)"/>
        <polygon points="138,50 176,24 170,18" fill="var(--orange-deep)"/>
        <polygon points="138,50 300,12 306,40 146,78" fill="var(--orange-ribbon)"/>
        <polygon points="300,12 336,6 326,22 340,34 306,40" fill="var(--orange-deep)" opacity=".85"/>
      </svg>
      <span class="price__line price__line--pay">Pay what you want</span>
      <span class="price__line price__line--min">Minimum $3</span>
    </div>
  </main>
</body>
</html>
```